Retail Jewelry Business Card Design Project

We are in need of a new business card design for a retail jewelry store. This store is in the business of fine jewelry including but not specific to bridal jewelry, diamonds, designer jewelry and watches.

This store has been in business for 20 years but continues to strive for a modern professional appeal. The main colors use for this business are a royal blue, white and silver.

Target Market(s)

Target market is ages 18-50

Industry/Entity Type

Jewelry

Requirements
Must have
• Sales Person Name
Sales Person Email Address

Store Address
Store Phone
Website

Standard business card size. No odd shapes or sizes.
Nice to have
• Overall modern feel for card.

We have thought that a design with a nice feature of the logo on the back of the card would be nice but open to ideas.
Should not have
• No specific images of jewelry should be used.

```html
<!DOCTYPE html>
<html lang="en">
<head>
<meta charset="utf-8">
<title>Marcus Hale Fine Jewelry – Business Card</title>
<link rel="stylesheet" href="https://fonts.googleapis.com/css2?family=Montserrat:wght@400;500&family=Gelasio:ital@1&display=swap">
<style>
  :root {
    --royal-blue: #2e3192;
    --silver-rule: #7a76c0;
    --paper: #ffffff;
    --backdrop: #ffffff;
    --shadow: rgba(0, 0, 0, 0.18);
  }
  * { margin: 0; padding: 0; box-sizing: border-box; }
  html, body {
    width: 980px;
    height: 1200px;
    overflow: hidden;
    background: var(--backdrop);
  }
  .presentation {
    position: relative;
    width: 980px;
    height: 1200px;
  }
  .card {
    position: absolute;
    left: 153px;
    width: 684px;
    height: 390px;
    box-shadow: 2px 4px 10px var(--shadow);
  }
  .card-front {
    top: 150px;
    background: var(--paper);
    display: flex;
    align-items: center;
    justify-content: center;
  }
  .wordmark {
    font-family: "Montserrat", sans-serif;
    font-weight: 500;
    color: var(--royal-blue);
    font-size: 40px;
    letter-spacing: 0.06em;
    text-transform: uppercase;
    text-align: center;
    line-height: 1.25;
  }
  .card-back {
    top: 670px;
    background: var(--royal-blue);
    color: var(--paper);
  }
  .contact-name {
    position: absolute;
    left: 46px;
    top: 108px;
    font-family: "Montserrat", sans-serif;
    font-weight: 500;
    font-size: 29px;
    letter-spacing: 0.05em;
    text-transform: uppercase;
  }
  .contact-email {
    position: absolute;
    left: 46px;
    top: 146px;
    font-family: "Montserrat", sans-serif;
    font-weight: 400;
    font-size: 23px;
  }
  .divider {
    position: absolute;
    left: 46px;
    top: 289px;
    width: 594px;
    height: 3px;
    background: var(--silver-rule);
  }
  .store-details {
    position: absolute;
    top: 308px;
    font-family: "Gelasio", serif;
    font-style: italic;
    font-size: 17px;
    line-height: 22px;
  }
  .store-address { left: 46px; }
  .store-reach { left: 334px; }
</style>
</head>
<body>
<main class="presentation">
  <section class="card card-front" aria-label="Card front">
    <h1 class="wordmark">Marcus Hale<br>Fine Jewelry</h1>
  </section>

  <section class="card card-back" aria-label="Card back">
    <p class="contact-name">Marcus Hale Whitford</p>
    <p class="contact-email">marcus@marcushalejewelry.com</p>
    <div class="divider"></div>
    <address class="store-details store-address">
      2280 Bayview Avenue<br>Lakeport, FL 32590
    </address>
    <p class="store-details store-reach">
      (555) 214-3087<br>www.marcushalejewelry.com
    </p>
  </section>
</main>
</body>
</html>
```